Flyer Design Project

We require a flyer designed for a LED Lighting Company, who developed and supply LED Bulbs,

K-ORB Ltd provide energy saving & environmentally friendly LED Lighting Solutions, which can be utilised indoors or outdoors, in both Private and commercial environments.

Generic LED products for direct replacement of incandescent, halogen & fluorescent lamps are readily available, offering energy savings of up to 80%

We also provide a tailored & effective design service to meet specific lighting needs, ensuring that the correct product is supplied to provide maximum lighting effect.

Flyer to be double sided, A5 size

Sample packaging is uploaded, this colour scheme would be preferred but also open to other options as it is not finalized yet

Reason: Deadline extended in order to allow time for updates to brief

Apologies for the lack of information in the brief, It will take me some days to get the time to make updates to this, so I expect to have to increase the deadline again.  Once I have the information updated I will also change the project to guaranteed.

Thanks

Tomas

Will be updating the brief over the coming days... Once finished the project status will be changed to guaranteed.

Thanks

Reason: will be on business trip in the coming days, so must extend deadline again in order to make time to review submitted designs and any changes that are needed.

• On back of flyer example of lights available with pictures
Tube lights
Spot lights (GU10, MR16)
Bulbs, Candle/Globe
Flood/security lights
Street lights

Also to be shown on flyer (position optional)
www.k-orblighting.co.uk
'Developed in United Kingdom by K-ORB LTD
'Keen Optics Radiant Beams' (1st letter of each word subtlety highlighted)
(T) + 44 28 391 62407
(F) + 44 28 391 62409
E-mail: k.orb@mailvex.com

• Benefits of LED Lighting:
Up to 80% Less Power consumption
Reduce Carbon Foot Print
50,000+ hours lifetime
Instant illumination
Environmentally friendly

```html
<!DOCTYPE html>
<html lang="en">
<head>
<meta charset="utf-8">
<title>K-ORB Ltd – LED Lighting Flyer</title>
<link href="https://fonts.googleapis.com/css2?family=Arimo:ital,wght@0,700;1,700&family=Tinos:wght@400;700&display=swap" rel="stylesheet">
<style>
  :root {
    --frame-green: #4caf48;
    --banner-yellow: #fff23a;
    --night-black: #000000;
    --sky-blue: #4ec6ee;
    --sky-blue-deep: #2f9fd0;
    --cord-light: #fdf7cf;
    --accent-yellow: #ffee1a;
    --text-white: #ffffff;
    --text-dark: #111111;
  }
  * { margin: 0; padding: 0; box-sizing: border-box; }
  html, body { width: 847px; height: 1200px; overflow: hidden; background: var(--frame-green); }
  .flyer {
    position: relative;
    width: 847px;
    height: 1200px;
    background: var(--frame-green);
    overflow: hidden;
  }
  .flyer__background { position: absolute; inset: 0; }
  .brand-title {
    position: absolute;
    left: 50px;
    top: 108px;
    font-family: "Arimo", Arial, sans-serif;
    font-weight: 700;
    font-size: 80px;
    line-height: 1;
    color: var(--text-white);
    letter-spacing: 1px;
  }
  .pendant-cord {
    position: absolute;
    left: 292px;
    top: 192px;
    width: 27px;
    height: 474px;
    background: linear-gradient(90deg, #e8dfa8, var(--cord-light) 45%, #ffffff 60%, #e3d99c);
  }
  .bulb-photo {
    position: absolute;
    left: 198px;
    top: 589px;
    width: 342px;
    height: 343px;
    background: radial-gradient(ellipse 45% 55% at 50% 48%, #e9e4c6 0%, #b8b190 30%, #3a372c 60%, #0a0a08 85%);
  }
  .acronym {
    position: absolute;
    left: 30px;
    top: 372px;
    font-family: "Tinos", "Times New Roman", serif;
    font-weight: 700;
    color: var(--text-white);
    font-size: 36px;
    line-height: 66px;
    list-style: none;
  }
  .acronym__initial {
    font-family: "Arimo", Arial, sans-serif;
    font-style: italic;
    font-size: 56px;
    color: var(--accent-yellow);
    margin-right: 8px;
  }
  .benefit {
    position: absolute;
    white-space: nowrap;
  }
  .benefit--headline {
    font-family: "Arimo", Arial, sans-serif;
    font-style: italic;
    font-weight: 700;
    font-size: 44px;
    color: var(--accent-yellow);
    letter-spacing: 0.5px;
  }
  .benefit--minor {
    font-family: "Tinos", "Times New Roman", serif;
    font-weight: 700;
    color: var(--text-white);
  }
  .benefit--energy { left: 383px; top: 383px; }
  .benefit--economical { left: 387px; top: 449px; }
  .benefit--eco { left: 375px; top: 530px; font-size: 22px; }
  .benefit--indoors { left: 549px; top: 600px; font-size: 25px; }
  .benefit--outdoors { left: 549px; top: 655px; font-size: 25px; }
  .contact {
    position: absolute;
    left: 80px;
    top: 1044px;
    font-family: "Tinos", "Times New Roman", serif;
    font-size: 27px;
    line-height: 41px;
    color: var(--text-dark);
  }
  .contact__gap { display: inline-block; width: 14px; }
</style>
</head>
<body>
  <main class="flyer">
    <svg class="flyer__background" width="847" height="1200" viewBox="0 0 847 1200" aria-hidden="true">
      <defs>
        <linearGradient id="skyFade" x1="0" y1="0" x2="1" y2="0">
          <stop offset="0" stop-color="var(--sky-blue-deep)"/>
          <stop offset="0.12" stop-color="var(--sky-blue)"/>
          <stop offset="1" stop-color="var(--sky-blue)"/>
        </linearGradient>
      </defs>
      <rect class="panel-yellow" x="20" y="20" width="807" height="272" fill="var(--banner-yellow)"/>
      <rect class="panel-black" x="20" y="292" width="807" height="656" fill="var(--night-black)"/>
      <rect class="panel-blue" x="20" y="948" width="807" height="232" fill="url(#skyFade)"/>
      <path class="panel-curve" d="M20 930 L590 930 Q600 1000 320 1028 Q100 1040 20 1010 Z" fill="var(--night-black)"/>
    </svg>

    <h1 class="brand-title">K - ORB LTD.</h1>

    <div class="pendant-cord" aria-hidden="true"></div>
    <div class="bulb-photo" role="img" aria-label="Photograph of a glowing spiral energy saving bulb hanging on a cord against a dark background"></div>

    <ul class="acronym">
      <li><span class="acronym__initial">K</span>EEN</li>
      <li><span class="acronym__initial">O</span>PTICS</li>
      <li><span class="acronym__initial">R</span>ADIANT</li>
      <li><span class="acronym__initial">B</span>EAMS</li>
    </ul>

    <p class="benefit benefit--headline benefit--energy">ENERGY SAVING</p>
    <p class="benefit benefit--headline benefit--economical">ECONOMICAL</p>
    <p class="benefit benefit--minor benefit--eco">ENVIRONMENTALLY FRIENDLY</p>
    <p class="benefit benefit--minor benefit--indoors">INDOORS</p>
    <p class="benefit benefit--minor benefit--outdoors">OUTDOORS</p>

    <address class="contact" style="font-style: normal;">
      Developed in the United kingdom by K-ORB LTD.<br>
      www.k-orblighting.co.uk<span class="contact__gap"></span>(T) + 44 28 391 62407<br>
      (F) + 44 28 391 62409<span class="contact__gap"></span>E-mail:<span class="contact__gap"></span>k.orb@mailvex.com
    </address>
  </main>
</body>
</html>
```